pressure washing advertisment

I would like front and back designed post cards. we offer pressure washing services for residential customers. I want to highlight before and after pictures as examples of our more popular services. I would also like to have our email www.bluhavenwashco.example and the facebook and Instagram logo somewhere. you can also include all major credit card logos as acceptable payments. I have attached our logo along with before and after pictures. also feel free to go to my website for any additional information that should be added to the post card. lastly I want a small promotion of $25 off any service somewhere.<br/><br/>Thank you!!

Target Market(s)

homeowners

Industry/Entity Type

Cleaning Service

Font styles to use
Serif
Sans Serif

Colors

Designer to choose colors to be used in the design.

Requirements
Must have
• before and after pictures with website and logo
Nice to have
• clean look that flows

```html
<!DOCTYPE html>
<html lang="en">
<head>
<meta charset="utf-8">
<title>Bluhaven Wash Co. – Postcard</title>
<link rel="stylesheet" href="https://fonts.googleapis.com/css2?family=Montserrat:wght@400;500;600;700;800&family=Oswald:wght@700&display=swap">
<style>
  :root {
    --navy: #0d3f7e;
    --navy-deep: #083670;
    --red: #e31f2a;
    --red-soft: rgba(214, 36, 46, 0.88);
    --white: #ffffff;
    --ink: #2b2b2b;
    --rule: #9a9a9a;
    --stamp: #ececec;
    --page: #f1f1ef;
  }
  * { box-sizing: border-box; margin: 0; padding: 0; }
  html, body {
    width: 1200px; height: 1200px; overflow: hidden;
    background: var(--page);
    font-family: "Montserrat", sans-serif;
  }
  .card {
    position: absolute; width: 744px; height: 495px;
    background: var(--white);
    box-shadow: 0 4px 14px rgba(0,0,0,0.18);
    overflow: hidden;
  }
  .card--back { left: 93px; top: 88px; }
  .card--front { left: 377px; top: 622px; }

  /* Back side */
  .services-panel {
    position: absolute; left: 0; top: 0; width: 352px; height: 495px;
    background: radial-gradient(ellipse at 40% 30%, #174c8c 0%, var(--navy-deep) 70%);
    color: var(--white);
  }
  .divider-red {
    position: absolute; left: 352px; top: 0; width: 4px; height: 495px;
    background: var(--red);
  }
  .services-title {
    position: absolute; left: 45px; top: 44px;
    font-size: 20px; font-weight: 800; letter-spacing: 0.3px;
  }
  .services-title span { color: var(--red); font-weight: 400; }
  .services-rule {
    position: absolute; left: 45px; top: 70px; width: 154px; height: 1px; background: rgba(255,255,255,0.7);
  }
  .services-rule::before {
    content: ""; position: absolute; left: 0; top: -1px; width: 14px; height: 3px; background: var(--red);
  }
  .service { position: absolute; left: 45px; width: 280px; }
  .service h3 { color: var(--red); font-size: 10px; font-weight: 600; margin-bottom: 9px; }
  .service p { font-size: 8px; line-height: 1.3; }
  .call-label { position: absolute; left: 46px; top: 371px; font-size: 10px; }
  .call-phone { position: absolute; left: 45px; top: 384px; font-size: 19px; font-weight: 600; letter-spacing: 0.5px; }
  .back-web { position: absolute; left: 46px; top: 416px; font-size: 9px; letter-spacing: 0.3px; }
  .house-photo {
    position: absolute; left: 0; top: 440px; width: 352px; height: 55px;
    background: linear-gradient(180deg, rgba(8,54,112,0) 0%, #6a6f7a 40%, #c9a978 100%);
  }

  .brand-name {
    position: absolute; color: var(--navy); font-weight: 700; white-space: nowrap;
    display: flex; align-items: center; gap: 6px;
  }
  .brand-name .mark { display: inline-block; background: var(--red); }
  .brand-name--back { left: 407px; top: 96px; font-size: 15px; }
  .brand-name--back .mark { width: 10px; height: 10px; }
  .stamp-box { position: absolute; left: 596px; top: 60px; width: 87px; height: 83px; background: var(--stamp); }
  .address-line { position: absolute; left: 407px; width: 273px; height: 1px; background: var(--rule); }

  /* Front side */
  .photo { position: absolute; }
  .photo--hero {
    left: 0; top: 22px; width: 412px; height: 270px;
    background: linear-gradient(180deg, #4f86d6 0%, #9bb5d8 25%, #e2cf8f 50%, #c9b27a 75%, #5f7a3c 100%);
  }
  .photo--before {
    left: 0; top: 304px; width: 196px; height: 168px;
    background: linear-gradient(180deg, #6b9fe0 0%, #a8bcd6 30%, #7c7f86 60%, #5b5e63 100%);
  }
  .photo--after {
    left: 214px; top: 304px; width: 198px; height: 168px;
    background: linear-gradient(180deg, #6b9fe0 0%, #b8c6d8 30%, #a7abb1 60%, #8d9095 100%);
  }
  .photo-label {
    position: absolute; left: 0; right: 0; top: 123px; height: 31px;
    background: var(--red-soft); color: var(--white);
    font-size: 20px; font-weight: 600; letter-spacing: 0.6px;
    display: flex; align-items: center; justify-content: center;
  }
  .brand-name--front { left: 452px; top: 66px; font-size: 20px; }
  .brand-name--front .mark { width: 14px; height: 14px; }
  .headline { position: absolute; left: 452px; top: 152px; width: 258px; color: var(--navy); line-height: 1; }
  .headline .h-pro { display: block; font-size: 29px; font-weight: 600; letter-spacing: 0.8px; }
  .headline .h-res { display: block; font-family: "Oswald", sans-serif; font-size: 46px; font-weight: 700; color: var(--red); line-height: 1.08; }
  .headline .h-wash { display: block; font-size: 22px; font-weight: 600; letter-spacing: 0.6px; }
  .headline .h-con { display: block; font-size: 33px; font-weight: 700; letter-spacing: 0.8px; margin-top: 4px; }
  .about-title { position: absolute; left: 453px; top: 323px; font-size: 20px; font-weight: 800; color: var(--navy); }
  .about-title span { color: var(--red); font-weight: 400; }
  .about-rule { position: absolute; left: 453px; top: 350px; width: 110px; height: 1px; background: #bbb; }
  .about-rule::before { content: ""; position: absolute; left: 0; top: -1px; width: 14px; height: 3px; background: var(--red); }
  .about-text {
    position: absolute; left: 453px; top: 365px; width: 252px;
    font-size: 9.5px; line-height: 1.3; color: var(--ink); text-align: justify;
  }
  .front-web { position: absolute; left: 453px; top: 463px; font-size: 9.5px; color: var(--ink); }
</style>
</head>
<body>

<section class="card card--back" aria-label="Postcard back">
  <div class="services-panel">
    <h2 class="services-title">OUR <span>SERVICES</span></h2>
    <div class="services-rule"></div>

    <div class="service" style="top:84px">
      <h3>Soft Wash House Washing</h3>
      <p>We use a soft wash method that removes mildew, algae, mold, and other organic stains from the exterior of your house.</p>
    </div>
    <div class="service" style="top:133px">
      <h3>Driveway &amp; Concrete Cleaning</h3>
      <p>Rejuvenate your property and remove dirt, grime, and other unwanted material with our expert exterior cleaning services.</p>
    </div>
    <div class="service" style="top:182px">
      <h3>Gutter Cleaning &amp; Brightening</h3>
      <p>Keep your gutters working correctly with a professional pressure washing service.</p>
    </div>
    <div class="service" style="top:234px">
      <h3>Deck &amp; Fence Cleaning</h3>
      <p>Rediscover outdoor living with professionally cleaned spaces..</p>
    </div>

    <div class="call-label">CALL US NOW</div>
    <div class="call-phone">555-014-2290</div>
    <div class="back-web">www.bluhavenwashco.example</div>

    <div class="house-photo" role="img" aria-label="Photo of a large two-storey home lit at dusk"></div>
  </div>
  <div class="divider-red"></div>

  <div class="brand-name brand-name--back"><span class="mark"></span>BLUHAVEN WASH CO.</div>
  <div class="stamp-box" aria-label="Stamp area"></div>
  <div class="address-line" style="top:208px"></div>
  <div class="address-line" style="top:264px"></div>
  <div class="address-line" style="top:318px"></div>
  <div class="address-line" style="top:372px"></div>
</section>

<section class="card card--front" aria-label="Postcard front">
  <div class="photo photo--hero" role="img" aria-label="Photo of a worker pressure washing the siding of a yellow two-storey house"></div>
  <div class="photo photo--before" role="img" aria-label="Before photo of a grey house entrance with stained walls">
    <div class="photo-label">BEFORE</div>
  </div>
  <div class="photo photo--after" role="img" aria-label="After photo of the same grey house entrance cleaned">
    <div class="photo-label">AFTER</div>
  </div>

  <div class="brand-name brand-name--front"><span class="mark"></span>BLUHAVEN WASH CO.</div>

  <h1 class="headline">
    <span class="h-pro">PROFESSIONAL</span>
    <span class="h-res">RESIDENTIAL</span>
    <span class="h-wash">PRESSURE WASHING</span>
    <span class="h-con">CONTRACTOR</span>
  </h1>

  <h2 class="about-title">ABOUT <span>US</span></h2>
  <div class="about-rule"></div>
  <p class="about-text">Since our founding, we’ve worked with numerous clients throughout the area. Great service begins and ends with experienced and friendly professionals, which is why we put so much consideration into the quality of our work and our customer's satisfaction.</p>
  <div class="front-web">www.bluhavenwashco.example</div>
</section>

</body>
</html>
```